US Higher Education Changes Infographic

Create an info graphic which visually demonstrates statistics from and industry study of college students/parents and higher education professionals.

This graphic should be visually pleasing and conform with our brand styles.

Illustrations/icons should not be too juvenile or cartoon

We prefer a vibrant crisp design and is impactful and not cluttered.

examples are attached for reference.

Target Market(s)

US higher education industry

Industry/Entity Type

College

Requirements
Must have
• 8x10 finished design
• use colors and fonts from style guide
Should not have
• cluttered design, juvenile images

```html
<!DOCTYPE html>
<html lang="en">
<head>
<meta charset="utf-8">
<title>The FAFSA Opens Early</title>
<link href="https://fonts.googleapis.com/css2?family=Montserrat:wght@600;700&family=Questrial&display=swap" rel="stylesheet">
<style>
  :root{
    --orange:#f7941d;
    --green:#6cbe45;
    --slate:#6d6e71;
    --ink:#4d4d4f;
    --pale:#c7c8ca;
    --white:#ffffff;
    --black:#1a1a1a;
  }
  *{margin:0;padding:0;box-sizing:border-box}
  html,body{width:848px;height:1200px;overflow:hidden;background:var(--white)}
  body{font-family:"Questrial",sans-serif;color:var(--ink)}
  .canvas{position:relative;width:848px;height:1200px;overflow:hidden}
  .abs{position:absolute}
  .title{left:102px;top:36px;font-family:"Questrial",sans-serif;font-size:40px;color:var(--orange);font-weight:400;letter-spacing:.3px;-webkit-text-stroke:1px var(--orange)}
  .title-rule{left:102px;top:88px;width:432px;height:1.5px;background:var(--slate)}
  .intro{left:102px;top:93px;font-size:21px;line-height:27.5px;color:var(--ink);-webkit-text-stroke:.3px var(--ink)}
  .intro em{font-style:normal;color:var(--green);-webkit-text-stroke:.3px var(--green)}
  .brand{left:600px;top:80px;display:flex;align-items:center;gap:8px}
  .brand-dot{width:14px;height:14px;border-radius:50%;background:var(--green)}
  .brand-name{font-family:"Montserrat",sans-serif;font-weight:700;font-size:32px;color:var(--black)}
  .band{left:24px;width:800px;height:64px;border-radius:24px 24px 0 0;display:flex;align-items:center;justify-content:center;color:var(--white);font-family:"Montserrat",sans-serif;font-weight:600;font-size:30px;letter-spacing:.2px}
  .band--green{top:191px;background:var(--green);height:65px}
  .band--slate{top:624px;background:var(--slate)}
  .kicker{font-family:"Montserrat",sans-serif;font-weight:700;font-size:17px;color:var(--green);line-height:23px;letter-spacing:.2px}
  .stat{font-family:"Montserrat",sans-serif;font-weight:700;color:var(--orange);font-size:28px;line-height:1}
  .copy{font-size:14px;line-height:16.5px;color:var(--ink)}
  .vdash{border-left:1.5px dashed var(--green)}
  .hdash{border-top:1.5px dashed var(--green)}
  .gdash{border-left:1.5px dashed var(--slate)}
  .gray-dash{border-top:1.2px dashed var(--slate)}
  .icon{border-radius:8px}
  .icon--slate{background:linear-gradient(160deg,#7a7b7e,#58595b)}
  .icon--mix{background:linear-gradient(135deg,#6d6e71 60%,var(--orange))}
  .icon--orange{background:linear-gradient(135deg,#6d6e71 30%,var(--orange))}
  .icon--greenmix{background:linear-gradient(135deg,#6d6e71 60%,var(--green))}
  .practices{left:0;top:932px;width:848px;height:268px;background:var(--orange)}
  .practices-frame{left:28px;top:978px;width:794px;height:170px;border:1.5px dashed var(--white);border-radius:16px}
  .practices-pill{left:176px;top:954px;width:478px;height:48px;border-radius:24px;background:var(--white);display:flex;align-items:center;justify-content:center;font-family:"Montserrat",sans-serif;font-weight:700;font-size:29px;color:var(--black)}
  .practice-copy{font-size:14.5px;line-height:16.5px;color:var(--black)}
  .practice-icon{background:rgba(255,255,255,.85);border-radius:10px}
  .wdash{border-left:1.5px dashed var(--white)}
  .footer{left:0;top:1160px;width:848px;text-align:center;color:var(--white);font-size:17px;letter-spacing:.2px}
</style>
</head>
<body>
<main class="canvas">

  <header>
    <h1 class="abs title">The FAFSA Opens Early</h1>
    <div class="abs title-rule"></div>
    <p class="abs intro">The <em>class of 2017</em> will begin filing their<br>FAFSA on <em>October 1st</em> using income and<br>tax <em>data from 2015</em></p>
    <div class="abs brand"><span class="brand-dot"></span><span class="brand-name">Veltrix</span></div>
  </header>

  <section class="students">
    <h2 class="abs band band--green">WHAT ARE STUDENTS AND FAMILIES SAYING?</h2>

    <div class="abs vdash" style="left:394px;top:272px;height:336px"></div>
    <div class="abs hdash" style="left:64px;top:466px;width:322px"></div>
    <div class="abs hdash" style="left:398px;top:484px;width:378px"></div>

    <!-- Cost -->
    <h3 class="abs kicker" style="left:102px;top:274px">COST IS A BIG FACTOR</h3>
    <svg class="abs" style="left:100px;top:310px" width="222" height="44" role="img" aria-label="Unit chart: 8 of 10 filled">
      <g fill="var(--orange)">
        <circle cx="10" cy="22" r="9"/><circle cx="32" cy="22" r="9"/><circle cx="54" cy="22" r="9"/><circle cx="76" cy="22" r="9"/>
        <circle cx="98" cy="22" r="9"/><circle cx="120" cy="22" r="9"/><circle cx="142" cy="22" r="9"/><circle cx="164" cy="22" r="9"/>
      </g>
      <g fill="var(--pale)"><circle cx="186" cy="22" r="9"/><circle cx="208" cy="22" r="9"/></g>
    </svg>
    <p class="abs copy" style="left:106px;top:360px">Of students who plan to apply<br>for financial aid</p>
    <div class="abs gray-dash" style="left:106px;top:395px;width:218px"></div>
    <span class="abs stat" style="left:104px;top:406px">76%</span>
    <p class="abs copy" style="left:170px;top:402px">indicated that cost was<br>an important factor in the<br>college selection process.</p>

    <!-- Earlier understanding -->
    <h3 class="abs kicker" style="left:102px;top:478px">EARLIER UNDERSTANDING</h3>
    <div class="abs icon icon--slate" style="left:94px;top:510px;width:54px;height:84px" role="img" aria-label="Icon: money bag with dollar sign"></div>
    <div class="abs icon icon--orange" style="left:158px;top:544px;width:52px;height:50px" role="img" aria-label="Icon: student with clock"></div>
    <span class="abs stat" style="left:155px;top:512px">69%</span>
    <p class="abs copy" style="left:225px;top:510px">believe an earlier<br>understanding of<br>cost and aid would<br>be helpful to their<br>planning process</p>

    <!-- Award letter -->
    <h3 class="abs kicker" style="left:454px;top:274px">EARLIER AWARD LETTER DELIVERY</h3>
    <svg class="abs" style="left:498px;top:304px" width="200" height="40" role="img" aria-label="Unit chart: 9 of 10 filled">
      <g fill="var(--orange)">
        <circle cx="9" cy="20" r="8"/><circle cx="29" cy="20" r="8"/><circle cx="49" cy="20" r="8"/><circle cx="69" cy="20" r="8"/><circle cx="89" cy="20" r="8"/>
        <circle cx="109" cy="20" r="8"/><circle cx="129" cy="20" r="8"/><circle cx="149" cy="20" r="8"/><circle cx="169" cy="20" r="8"/>
      </g>
      <circle cx="189" cy="20" r="8" fill="var(--pale)"/>
    </svg>
    <div class="abs icon icon--mix" style="left:404px;top:346px;width:84px;height:68px" role="img" aria-label="Icon: clock and signed document"></div>
    <span class="abs stat" style="left:501px;top:350px;font-size:25px">89%</span>
    <p class="abs copy" style="left:556px;top:347px">want their award<br>letter earlier</p>
    <div class="abs gray-dash" style="left:502px;top:381px;width:224px"></div>
    <svg class="abs" style="left:502px;top:390px" width="170" height="32" role="img" aria-label="Unit chart: 4 of 10 filled">
      <g fill="var(--orange)"><circle cx="8" cy="16" r="7"/><circle cx="25" cy="16" r="7"/><circle cx="42" cy="16" r="7"/><circle cx="59" cy="16" r="7"/></g>
      <g fill="var(--pale)"><circle cx="76" cy="16" r="7"/><circle cx="93" cy="16" r="7"/><circle cx="110" cy="16" r="7"/><circle cx="127" cy="16" r="7"/><circle cx="144" cy="16" r="7"/><circle cx="161" cy="16" r="7"/></g>
    </svg>
    <span class="abs stat" style="left:500px;top:427px;font-size:25px">41%</span>
    <p class="abs copy" style="left:554px;top:426px">want their award letter in the<br>fall semester of their Senior<br>Year</p>

    <!-- Transparency -->
    <h3 class="abs kicker" style="left:457px;top:495px">MORE TRANSPARENCY</h3>
    <div class="abs icon icon--slate" style="left:460px;top:524px;width:108px;height:84px" role="img" aria-label="Icon: college building with magnifying glass"></div>
    <span class="abs stat" style="left:582px;top:522px">82%</span>
    <p class="abs copy" style="left:581px;top:550px">would think more positively<br>about a college that<br>provided earlier insight</p>
  </section>

  <section class="colleges">
    <h2 class="abs band band--slate">HOW ARE COLLEGES RESPONDING?</h2>
    <div class="abs gdash" style="left:286px;top:704px;height:212px"></div>
    <div class="abs gdash" style="left:543px;top:704px;height:212px"></div>

    <h3 class="abs kicker" style="left:67px;top:704px">PLANNING TO<br>CHANGE</h3>
    <div class="abs icon icon--greenmix" style="left:70px;top:764px;width:90px;height:68px" role="img" aria-label="Icon: college building with refresh arrows"></div>
    <span class="abs stat" style="left:172px;top:776px">68%</span>
    <p class="abs copy" style="left:172px;top:810px">plan to make<br>significant<br>changes as a<br>result of PPY<br>and early<br>FAFSA in 2016.</p>

    <h3 class="abs kicker" style="left:305px;top:704px">DELIVERING EARLIER<br>INSIGHTS</h3>
    <div class="abs icon icon--greenmix" style="left:310px;top:764px;width:86px;height:88px" role="img" aria-label="Icon: hand holding a document and clock"></div>
    <span class="abs stat" style="left:409px;top:779px">77%</span>
    <p class="abs copy" style="left:409px;top:813px">plan to shift their<br>delivery of<br>financial aid<br>eligibility<br>information<br>earlier</p>

    <h3 class="abs kicker" style="left:565px;top:704px">CONSEQUENCES OF<br>INACTION</h3>
    <div class="abs icon icon--greenmix" style="left:560px;top:764px;width:96px;height:80px" role="img" aria-label="Icon: college building with thumbs down"></div>
    <span class="abs stat" style="left:668px;top:764px">80%</span>
    <p class="abs copy" style="left:671px;top:800px">believe that<br>institutions that DO<br>NOT shift their cycle<br>earlier will be at a<br>competitive<br>disadvantage</p>
  </section>

  <section class="abs practices" aria-label="Emerging best practices"></section>
  <div class="abs practices-frame"></div>
  <h2 class="abs practices-pill">EMERGING BEST PRACTICES</h2>

  <div class="abs practice-icon" style="left:50px;top:1020px;width:68px;height:92px" role="img" aria-label="Icon: presenter with clock and audience"></div>
  <p class="abs practice-copy" style="left:130px;top:1038px">Address ‘the cost<br>question’ earlier in<br>outreach and nurturing<br>campaigns.</p>
  <div class="abs wdash" style="left:298px;top:1030px;height:100px"></div>

  <div class="abs practice-icon" style="left:312px;top:1028px;width:92px;height:92px" role="img" aria-label="Icon: balance scale weighing money and books"></div>
  <p class="abs practice-copy" style="left:414px;top:1038px">Communicate<br>cost alongside<br>personalized<br>value content</p>
  <div class="abs wdash" style="left:542px;top:1030px;height:100px"></div>

  <div class="abs practice-icon" style="left:548px;top:1036px;width:76px;height:64px" role="img" aria-label="Icon: two people in conversation"></div>
  <p class="abs practice-copy" style="left:637px;top:1034px">Extend communications<br>programs to nurture<br>relationships with<br>prospective students<br>along the way.</p>

  <footer class="abs footer">555.014.2288 &nbsp;|&nbsp;hello@veltrix-media.com &nbsp;|&nbsp; www.veltrix-media.com</footer>

</main>
</body>
</html>
```